PELMARK
stationery items
Professional
Karim Doulani
Managing Director
Corniva Plaza L27
Al Fannar Road
P.O. Box 58214
Dubai - UAE
kdoulani@pelmark-gulfa.com
www.pelmark-gulfa.com
looking for full stationery items (business cards, letter heads, envelopes)
LOGO
Strategy Think-tank & Real Estate Asset Management Solutions
full package of logo

```html
<!DOCTYPE html>
<html lang="en">
<head>
<meta charset="utf-8">
<title>Pelmark Business Cards</title>
<link href="https://fonts.googleapis.com/css2?family=PT+Sans:wght@400;700&display=swap" rel="stylesheet">
<style>
  :root {
    --maroon: #7b2141;
    --maroon-deep: #6e1b38;
    --ink: #333333;
    --muted: #555555;
    --grey-band: #c4c4c4;
    --card-border: #c9c9c9;
    --paper: #ffffff;
  }
  * { box-sizing: border-box; margin: 0; padding: 0; }
  html, body { width: 1200px; height: 722px; overflow: hidden; background: var(--paper); }
  body { position: relative; font-family: "PT Sans", Arial, sans-serif; color: var(--ink); }

  .card {
    position: absolute;
    width: 560px;
    height: 344px;
    background: var(--paper);
    border: 1px solid var(--card-border);
    overflow: hidden;
  }
  .card--front-maroon { left: 20px; top: 2px; }
  .card--front-grey   { left: 618px; top: 2px; }
  .card--back-maroon  { left: 20px; top: 376px; background: var(--maroon); border-color: var(--maroon); }
  .card--back-white   { left: 618px; top: 376px; }

  .wordmark {
    position: absolute;
    display: flex;
    align-items: center;
    gap: 10px;
    color: var(--maroon);
    font-weight: 700;
    letter-spacing: 2px;
  }
  .wordmark__dot { width: 14px; height: 14px; background: var(--maroon); }
  .card--front-maroon .wordmark,
  .card--front-grey .wordmark { left: 40px; top: 70px; font-size: 34px; }

  .holder { position: absolute; left: 292px; top: 26px; }
  .holder__name { font-size: 30px; font-weight: 400; color: var(--maroon); line-height: 1.1; }
  .holder__title { font-size: 17px; color: var(--ink); margin-top: 8px; }

  .contact { position: absolute; left: 300px; top: 168px; font-size: 15px; line-height: 19px; color: var(--ink); list-style: none; }
  .contact__row { display: flex; align-items: center; gap: 6px; }
  .contact__row--plain { padding-left: 0; }
  .contact__icon { width: 13px; height: 13px; flex: none; }

  .band { position: absolute; left: 0; right: 0; bottom: 0; height: 22px; }
  .band--maroon { background: var(--maroon-deep); }
  .band--grey { background: var(--grey-band); }

  .logo-plate {
    position: absolute;
    left: 40px; top: 112px;
    width: 300px; height: 140px;
    background: var(--paper);
    display: flex; align-items: center; justify-content: center;
  }
  .logo-plate .wordmark { position: static; font-size: 46px; }

  .card--back-white .wordmark { right: 30px; bottom: 48px; font-size: 40px; }
</style>
</head>
<body>

<section class="card card--front-maroon" aria-label="Business card front, maroon edition">
  <div class="wordmark"><span class="wordmark__dot"></span>PELMARK</div>
  <div class="holder">
    <h1 class="holder__name">Karim Doulani</h1>
    <p class="holder__title">Managing Director</p>
  </div>
  <ul class="contact">
    <li>Corniva Plaza L27</li>
    <li>Al Fannar Road</li>
    <li>P.O. Box 58214, Dubai - UAE</li>
    <li class="contact__row">
      <svg class="contact__icon" viewBox="0 0 14 14"><path d="M3 1h3l1 3-2 1c1 2 2 3 4 4l1-2 3 1v3c0 1-1 2-2 2C6 13 1 8 1 3c0-1 1-2 2-2z" fill="var(--maroon)"/></svg>
      +971 4 286 5190</li>
    <li class="contact__row">
      <svg class="contact__icon" viewBox="0 0 14 14"><rect x="4" y="1" width="6" height="12" rx="1" fill="none" stroke="var(--maroon)" stroke-width="1.4"/><circle cx="7" cy="11" r="0.8" fill="var(--maroon)"/></svg>
      +971 55 718 4402</li>
    <li class="contact__row">
      <svg class="contact__icon" viewBox="0 0 14 14"><rect x="2" y="5" width="10" height="7" fill="none" stroke="var(--maroon)" stroke-width="1.3"/><rect x="4" y="1.5" width="6" height="4" fill="none" stroke="var(--maroon)" stroke-width="1.3"/></svg>
      +971 4 286 5190</li>
    <li class="contact__row">
      <svg class="contact__icon" viewBox="0 0 14 14"><rect x="1" y="3" width="12" height="8" fill="none" stroke="var(--maroon)" stroke-width="1.3"/><path d="M1 3l6 5 6-5" fill="none" stroke="var(--maroon)" stroke-width="1.3"/></svg>
      kdoulani@pelmark-gulfa.com</li>
    <li class="contact__row">
      <svg class="contact__icon" viewBox="0 0 14 14"><circle cx="7" cy="7" r="5.5" fill="none" stroke="var(--maroon)" stroke-width="1.3"/><path d="M1.5 7h11M7 1.5c-3 3-3 8 0 11M7 1.5c3 3 3 8 0 11" fill="none" stroke="var(--maroon)" stroke-width="1"/></svg>
      www.pelmark-gulfa.com</li>
  </ul>
  <div class="band band--maroon"></div>
</section>

<section class="card card--front-grey" aria-label="Business card front, grey edition">
  <div class="wordmark"><span class="wordmark__dot"></span>PELMARK</div>
  <div class="holder">
    <h2 class="holder__name">Karim Doulani</h2>
    <p class="holder__title">Managing Director</p>
  </div>
  <ul class="contact">
    <li>Corniva Plaza L27</li>
    <li>Al Fannar Road</li>
    <li>P.O. Box 58214, Dubai - UAE</li>
    <li class="contact__row">
      <svg class="contact__icon" viewBox="0 0 14 14"><path d="M3 1h3l1 3-2 1c1 2 2 3 4 4l1-2 3 1v3c0 1-1 2-2 2C6 13 1 8 1 3c0-1 1-2 2-2z" fill="var(--maroon)"/></svg>
      +971 4 286 5190</li>
    <li class="contact__row">
      <svg class="contact__icon" viewBox="0 0 14 14"><rect x="4" y="1" width="6" height="12" rx="1" fill="none" stroke="var(--maroon)" stroke-width="1.4"/><circle cx="7" cy="11" r="0.8" fill="var(--maroon)"/></svg>
      +971 55 718 4402</li>
    <li class="contact__row">
      <svg class="contact__icon" viewBox="0 0 14 14"><rect x="2" y="5" width="10" height="7" fill="none" stroke="var(--maroon)" stroke-width="1.3"/><rect x="4" y="1.5" width="6" height="4" fill="none" stroke="var(--maroon)" stroke-width="1.3"/></svg>
      +971 4 286 5190</li>
    <li class="contact__row">
      <svg class="contact__icon" viewBox="0 0 14 14"><rect x="1" y="3" width="12" height="8" fill="none" stroke="var(--maroon)" stroke-width="1.3"/><path d="M1 3l6 5 6-5" fill="none" stroke="var(--maroon)" stroke-width="1.3"/></svg>
      kdoulani@pelmark-gulfa.com</li>
    <li class="contact__row">
      <svg class="contact__icon" viewBox="0 0 14 14"><circle cx="7" cy="7" r="5.5" fill="none" stroke="var(--maroon)" stroke-width="1.3"/><path d="M1.5 7h11M7 1.5c-3 3-3 8 0 11M7 1.5c3 3 3 8 0 11" fill="none" stroke="var(--maroon)" stroke-width="1"/></svg>
      www.pelmark-gulfa.com</li>
  </ul>
  <div class="band band--grey"></div>
</section>

<section class="card card--back-maroon" aria-label="Business card back, maroon">
  <div class="logo-plate">
    <div class="wordmark"><span class="wordmark__dot"></span>PELMARK</div>
  </div>
</section>

<section class="card card--back-white" aria-label="Business card back, white">
  <div class="wordmark"><span class="wordmark__dot"></span>PELMARK</div>
</section>

</body>
</html>
```